B2B Energy Broker Website

Our current website looks amateur, we need something far more professional looking and advanced. Current website is www.kelmora-utilitylink.com

```html
<!DOCTYPE html>
<html lang="en">
<head>
<meta charset="utf-8">
<title>Kelmora UtilityLink — Transparent Energy Savings</title>
<link href="https://fonts.googleapis.com/css2?family=Arimo:wght@400;700&family=Lato:wght@400;700&family=Montserrat:wght@600;700&display=swap" rel="stylesheet">
<style>
:root{
  --navy:#1b1e4b;
  --navy-deep:#14173d;
  --ink:#2a2a3a;
  --muted:#4a4a55;
  --white:#ffffff;
  --pale:#dfe3e9;
  --line:#e6e7ee;
}
*{box-sizing:border-box;margin:0;padding:0}
html,body{width:1200px;height:4149px;overflow:hidden;background:var(--white)}
body{font-family:"Lato",sans-serif;color:var(--ink)}
.page{position:relative;width:1200px;height:4149px;overflow:hidden}
.band{position:absolute;left:0;width:1200px}
.torn{position:absolute;left:0;width:1200px;height:40px;display:block}

/* top bar */
.topbar{top:0;height:36px;background:var(--navy);color:#fff;font-size:15px;display:flex;justify-content:flex-end;align-items:center;gap:36px;padding-right:110px}
.topbar span{display:flex;align-items:center;gap:8px}
.topbar svg{width:22px;height:22px}

/* header */
.header{top:36px;height:94px;background:#fff;display:flex;align-items:center;padding:0 110px}
.brand{display:flex;align-items:center;gap:12px;font-family:"Arimo",sans-serif;font-size:26px;color:#3a3a3a;letter-spacing:1px}
.brand-dot{width:70px;height:70px;border-radius:50%;background:#3a3a3a}
.nav{margin-left:auto;display:flex;align-items:center;gap:35px;font-family:"Arimo",sans-serif;font-size:17px;color:var(--navy)}
.nav .active{font-weight:700}
.btn{display:inline-flex;align-items:center;justify-content:center;background:var(--navy);color:#fff;font-family:"Arimo",sans-serif;font-size:17px;border-radius:30px}
.nav .btn{width:153px;height:54px;margin-left:0}

/* hero */
.hero{top:130px;height:600px;text-align:center;color:#fff}
.hero-photo{position:absolute;inset:0;background:linear-gradient(180deg,#2c3f58 0%,#55708f 35%,#c7cfd8 70%,#8d96a2 100%)}
.hero-ring{position:absolute;left:575px;top:145px;width:50px;height:50px;border:3px solid #fff;border-radius:50%}
.hero h1{position:absolute;top:228px;width:100%;font-family:"Montserrat",sans-serif;font-weight:700;font-size:38px;letter-spacing:.5px}
.hero h2{position:absolute;top:287px;width:100%;font-family:"Montserrat",sans-serif;font-weight:700;font-size:26px}
.hero .btn.outline{position:absolute;left:522px;top:347px;width:156px;height:54px;background:rgba(27,30,75,.55);border:2px solid #fff;font-size:17px}
.dots{position:absolute;top:526px;left:556px;display:flex;gap:12px}
.dots i{width:20px;height:3px;background:#fff;display:block}
.dots i:first-child{background:#ccd}

/* section titles */
.title{position:absolute;width:100%;text-align:center;font-family:"Arimo",sans-serif;font-weight:700;font-size:39px;display:flex;justify-content:center;align-items:center;gap:22px}
.title::before,.title::after{content:"";width:75px;height:2px;background:currentColor}
.on-navy{color:#fff}
.on-white{color:var(--navy)}

/* about */
.about{top:730px;height:557px;background:#fff}
.about h2{position:absolute;left:110px;top:83px;font-family:"Arimo",sans-serif;font-size:40px;color:var(--navy);display:flex;align-items:center;gap:10px}
.about h2::after{content:"";width:100px;height:2px;background:var(--navy);margin-top:18px}
.about p{position:absolute;left:110px;top:150px;width:466px;font-size:17px;line-height:30px;text-align:justify;color:var(--muted)}
.about .btn{position:absolute;left:109px;top:420px;width:153px;height:54px}
.about-photo{position:absolute;left:673px;top:75px;width:412px;height:412px;border-radius:50%;background:#5e6289;padding:20px}
.about-photo div{width:100%;height:100%;border-radius:50%;background:linear-gradient(135deg,#1e4a8c,#4f85c8 45%,#a9c6e4 70%,#3e6aa3)}

/* services */
.services{top:1287px;height:661px;background:radial-gradient(ellipse at 60% 40%,#232866,var(--navy-deep))}
.svc-grid{position:absolute;left:110px;top:185px;display:flex;gap:21px}
.svc{width:229px;height:399px;background:#fff;border-radius:12px;text-align:center;padding:26px 22px 0}
.svc .ico{width:106px;height:106px;margin:0 auto;border-radius:50%;border:3px solid var(--navy);padding:6px}
.svc .ico div{width:100%;height:100%;border-radius:50%;background:var(--navy);display:flex;align-items:center;justify-content:center}
.svc h3{font-family:"Arimo",sans-serif;font-size:17px;color:var(--navy);margin-top:20px;line-height:26px;min-height:52px}
.svc p{font-family:"Arimo",sans-serif;font-size:14.5px;line-height:21.5px;color:var(--muted);margin-top:8px;text-align:justify;text-align-last:center}

/* partners */
.partners{top:1948px;height:380px;background:#fff}
.partner-row{position:absolute;left:111px;top:192px;display:flex;gap:31px}
.partner{width:221px;height:113px;background:#fff;border-radius:8px;box-shadow:0 2px 10px rgba(0,0,0,.18);display:flex;align-items:center;justify-content:center}
.partner span{display:block;width:140px;height:36px;border-radius:18px;background:#d7dbe4}

/* benefits */
.benefits{top:2328px;height:640px;background:radial-gradient(ellipse at 40% 40%,#242a6a,var(--navy-deep))}
.ben-grid{position:absolute;left:111px;top:187px;display:flex;gap:33px}
.ben{width:303px;height:375px;background:#fff;border-radius:0 0 60px 60px;text-align:center;overflow:hidden}
.ben .cap{height:140px;background:var(--pale);border-radius:0 0 70px 70px;display:flex;align-items:center;justify-content:center}
.ben h3{font-family:"Arimo",sans-serif;font-size:21px;color:#1a1a2a;margin-top:20px}
.ben p{font-family:"Arimo",sans-serif;font-size:16.5px;line-height:30px;color:var(--muted);padding:10px 36px 0}

/* faq */
.faq{top:2963px;height:840px}
.faq-photo{position:absolute;inset:0;background:linear-gradient(180deg,#eef1f5 0%,#e4e8ee 70%,#a77c57 85%,#6b4a30 100%)}
.faq .title{top:75px}
.acc{position:absolute;left:541px;width:547px;background:#fff;border-radius:45px;box-shadow:0 3px 12px rgba(0,0,0,.12);padding:28px 46px}
.acc h4{font-family:"Lato",sans-serif;font-weight:700;font-size:16px;line-height:29px;color:var(--navy);padding-right:40px;position:relative}
.acc h4 svg{position:absolute;right:-14px;top:2px;width:24px;height:24px}
.acc p{font-size:17px;line-height:30px;color:var(--muted);margin-top:14px;text-align:justify}
.faq .btn{position:absolute;left:541px;top:724px;width:155px;height:57px}

/* footer */
.footer{top:3803px;height:346px;background:var(--navy);color:#fff}
.foot-nav{position:absolute;top:42px;width:100%;display:flex;justify-content:center;gap:28px;font-size:17px}
.foot-cols{position:absolute;top:110px;left:0;width:1200px;display:flex}
.foot-col{flex:1;text-align:center;font-size:17px;line-height:30px;height:170px}
.foot-col + .foot-col{border-left:1px solid rgba(255,255,255,.35)}
.foot-col .ico{width:54px;height:54px;margin:10px auto 22px;border-radius:50%;border:2px solid #fff;display:flex;align-items:center;justify-content:center}
.foot-col b{font-weight:700}
.copy{position:absolute;top:304px;width:100%;text-align:center;font-size:17px}
</style>
</head>
<body>
<div class="page">

<svg width="0" height="0" style="position:absolute">
  <defs>
    <path id="tear" d="M0,40 L0,14 L22,20 L40,9 L63,18 L85,11 L104,24 L128,13 L150,19 L170,8 L196,21 L220,12 L242,18 L262,7 L288,22 L310,14 L331,19 L355,9 L378,23 L400,12 L420,18 L446,8 L468,20 L490,13 L512,24 L535,10 L558,17 L580,9 L604,22 L626,12 L648,19 L670,7 L694,21 L716,13 L737,18 L760,10 L784,23 L806,12 L828,20 L850,8 L874,19 L896,13 L918,24 L940,10 L962,18 L986,9 L1008,22 L1030,12 L1052,19 L1075,8 L1098,21 L1120,13 L1142,18 L1165,10 L1185,20 L1200,12 L1200,40 Z"/>
  </defs>
</svg>

<!-- Top contact bar -->
<div class="band topbar">
  <span><svg viewBox="0 0 24 24"><circle cx="12" cy="12" r="11" fill="#fff"/><path d="M8 6.5l2 .2.8 2.6-1.3 1a7 7 0 003.2 3.2l1-1.3 2.6.8.2 2a1.5 1.5 0 01-1.6 1.5A9.5 9.5 0 016.5 8.1 1.5 1.5 0 018 6.5z" fill="#1b1e4b"/></svg>0333 410 7265</span>
  <span><svg viewBox="0 0 24 24"><circle cx="12" cy="12" r="11" fill="#fff"/><rect x="6.5" y="8" width="11" height="8" rx="1" fill="#1b1e4b"/><path d="M6.8 8.6l5.2 4 5.2-4" stroke="#fff" stroke-width="1.2" fill="none"/></svg>info@kelmora-utilitylink.com</span>
</div>

<!-- Header -->
<header class="band header">
  <div class="brand"><span class="brand-dot"></span>Kelmora UtilityLink</div>
  <nav class="nav">
    <span class="active">Home</span><span>About Us</span><span>Services</span><span>FAQs</span><span>Contact Us</span>
    <span class="btn">GET STARTED</span>
  </nav>
</header>

<!-- Hero -->
<section class="band hero">
  <div class="hero-photo" role="img" aria-label="Snow-covered mountain peak under a dark blue sky"></div>
  <div class="hero-ring"></div>
  <h1>TRANSPARENT ENERGY SAVINGS</h1>
  <h2>UNBIASED FOR YOUR BUSINESS</h2>
  <span class="btn outline">GET STARTED</span>
  <div class="dots"><i></i><i></i><i></i></div>
  <svg class="torn" style="top:565px" viewBox="0 0 1200 40" preserveAspectRatio="none"><use href="#tear" fill="#fff"/></svg>
</section>

<!-- About -->
<section class="band about">
  <h2>About Us</h2>
  <p>Along with providing competitive business energy procurement, we run a complete service solution for your ongoing energy requirements. We can take total management of your bills, supplier relationship, renewals and more. If you are concerned about a more complex arrangement for your energy supply then we will endeavour to take over the time spent on it and allow you as much or as little involvement as you desire.</p>
  <span class="btn">GET STARTED</span>
  <div class="about-photo"><div role="img" aria-label="Engineer in a hard hat standing among solar panels"></div></div>
</section>

<!-- Services -->
<section class="band services">
  <div class="title on-navy" style="top:75px">Our Services</div>
  <div class="svc-grid">
    <div class="svc">
      <div class="ico"><div><svg width="34" height="40" viewBox="0 0 34 40"><path d="M17 2c2 8 12 13 12 24a12 12 0 01-24 0c0-6 4-9 5-14 2 4 4 5 4 5 2-5 2-10 3-15z" fill="#fff"/></svg></div></div>
      <h3>COMMERCIAL GAS</h3>
      <p>We offer an impartial review of your business gas requirements to ensure you are getting the best prices, service and management as a total package.</p>
    </div>
    <div class="svc">
      <div class="ico"><div><svg width="48" height="48" viewBox="0 0 48 48"><circle cx="24" cy="24" r="17" stroke="#fff" stroke-width="3" fill="none"/><rect x="18" y="14" width="3" height="8" fill="#fff"/><rect x="27" y="14" width="3" height="8" fill="#fff"/><path d="M15 21h18v4a9 9 0 01-18 0z" fill="#fff"/><rect x="22.5" y="33" width="3" height="6" fill="#fff"/></svg></div></div>
      <h3>COMMERCIAL ELECTRICITY</h3>
      <p>We offer an impartial review of your business electricity requirements to ensure you are getting the best prices, service and management as a total package.</p>
    </div>
    <div class="svc">
      <div class="ico"><div><svg width="46" height="46" viewBox="0 0 46 46"><g fill="#fff" transform="translate(23 23)"><circle r="12"/><rect x="-4" y="-19" width="8" height="38"/><rect x="-4" y="-19" width="8" height="38" transform="rotate(45)"/><rect x="-4" y="-19" width="8" height="38" transform="rotate(90)"/><rect x="-4" y="-19" width="8" height="38" transform="rotate(135)"/></g><circle cx="23" cy="23" r="5" fill="#1b1e4b"/></svg></div></div>
      <h3>UTILITY SERVICES</h3>
      <p>We can provide a wide range of business utility management services to ensure your time and money is better spent.</p>
    </div>
    <div class="svc">
      <div class="ico"><div><svg width="30" height="40" viewBox="0 0 30 40"><path d="M15 2C20 12 27 19 27 27a12 12 0 01-24 0C3 19 10 12 15 2z" fill="#fff"/></svg></div></div>
      <h3>COMMERCIAL WATER</h3>
      <p>The commercial water market has now been de-regulated. Speak to our team to find out how we can save you money on your water and waste bills.</p>
    </div>
  </div>
  <svg class="torn" style="top:622px" viewBox="0 0 1200 40" preserveAspectRatio="none"><use href="#tear" fill="#fff"/></svg>
</section>

<!-- Partners -->
<section class="band partners">
  <div class="title on-white" style="top:82px">Our Partner</div>
  <div class="partner-row">
    <div class="partner"><span></span></div>
    <div class="partner"><span></span></div>
    <div class="partner"><span></span></div>
    <div class="partner"><span></span></div>
  </div>
</section>

<!-- Benefits -->
<section class="band benefits">
  <div class="title on-navy" style="top:75px">Our Benefits</div>
  <div class="ben-grid">
    <div class="ben">
      <div class="cap"><svg width="76" height="70" viewBox="0 0 76 70" fill="none" stroke="#1b1e4b" stroke-width="3"><path d="M4 66h70"/><rect x="8" y="42" width="9" height="24"/><rect x="22" y="34" width="9" height="32"/><rect x="36" y="38" width="9" height="28"/><rect x="50" y="24" width="9" height="42"/><rect x="64" y="14" width="9" height="52"/><path d="M8 32l16-12 12 8 26-22"/><path d="M54 5h9v9"/></svg></div>
      <h3>Market Trend Analysis</h3>
      <p>Our energy analysts monitor a live energy market curve to ensure you buy at the right time and save as much as possible.</p>
    </div>
    <div class="ben">
      <div class="cap"><svg width="120" height="70" viewBox="0 0 120 70" fill="none" stroke="#1b1e4b" stroke-width="3.5" stroke-linejoin="round"><path d="M4 20l18-12 14 8 18-6 14 10"/><path d="M116 20L98 8 84 16"/><path d="M22 8l-18 12 10 22 10 8"/><path d="M98 8l18 12-10 22"/><path d="M54 10L40 24a5 5 0 007 6l14-10 32 24a5 5 0 01-7 7"/><path d="M86 51a5 5 0 01-7 7l-8-6M79 58a5 5 0 01-7 6l-6-5M66 64a5 5 0 01-7 4l-5-4"/><path d="M24 50a5 5 0 007 7l5-4a5 5 0 007 6l4-3a5 5 0 007 5"/></svg></div>
      <h3>Direct Relationships</h3>
      <p>We hold direct relationships with over 18 major suppliers, we use these to ensure you get the most from your supplier.</p>
    </div>
    <div class="ben">
      <div class="cap"><svg width="80" height="80" viewBox="0 0 80 80" fill="none" stroke="#1b1e4b" stroke-width="2.5"><path d="M40 3l3 6 6 1-5 4 1 6-5-3-5 3 1-6-5-4 6-1z"/><path d="M14 13l3 6 6 1-5 4 1 6-5-3-5 3 1-6-5-4 6-1z"/><path d="M66 13l3 6 6 1-5 4 1 6-5-3-5 3 1-6-5-4 6-1z"/><circle cx="40" cy="40" r="10"/><path d="M20 76v-10a12 12 0 0112-12h16a12 12 0 0112 12v10z"/><path d="M40 54v12"/><circle cx="17" cy="45" r="6"/><circle cx="63" cy="45" r="6"/><path d="M4 72v-6a9 9 0 019-9h6M76 72v-6a9 9 0 00-9-9h-6"/></svg></div>
      <h3>Industry Experience</h3>
      <p>Our two founders hold over 30 years industry experience between them and our staff are what we believe to be the best in the industry.</p>
    </div>
  </div>
  <svg class="torn" style="top:600px" viewBox="0 0 1200 40" preserveAspectRatio="none"><use href="#tear" fill="#eef1f5"/></svg>
</section>

<!-- FAQ -->
<section class="band faq">
  <div class="faq-photo" role="img" aria-label="Wind turbines standing on a dry hillside under a pale sky"></div>
  <div class="title on-white">FAQ</div>
  <div class="acc" style="top:172px">
    <h4>1. WHY SHOULD MY BUSINESS USE KELMORA UTILITYLINK SOLUTIONS?<svg viewBox="0 0 24 24"><circle cx="12" cy="12" r="11" fill="#1b1e4b"/><rect x="6" y="10.5" width="12" height="3" fill="#fff"/></svg></h4>
    <p>We provide an unbiased &amp; transparent cost effective solution to all your business energy needs. In essence, with over 3 decades experience in the UK energy Industry. We have both the expertise &amp; know how to manage your business energy requirements. Our philosophy is simple solutions with transparency.</p>
  </div>
  <div class="acc" style="top:507px;height:88px;padding-top:18px">
    <h4>2. WHO SHOULD CONSIDER USING KELMORA UTILITYLINK SOLUTIONS?<svg viewBox="0 0 24 24"><circle cx="12" cy="12" r="11" fill="#1b1e4b"/><rect x="6" y="10.5" width="12" height="3" fill="#fff"/><rect x="10.5" y="6" width="3" height="12" fill="#fff"/></svg></h4>
  </div>
  <div class="acc" style="top:613px;height:89px;padding-top:22px">
    <h4>2. IS KELMORA UTILITYLINK SOLUTIONS INDEPENDENT?<svg viewBox="0 0 24 24"><circle cx="12" cy="12" r="11" fill="#1b1e4b"/><rect x="6" y="10.5" width="12" height="3" fill="#fff"/><rect x="10.5" y="6" width="3" height="12" fill="#fff"/></svg></h4>
  </div>
  <span class="btn">VIEW ALL</span>
</section>

<!-- Footer -->
<footer class="band footer">
  <div class="foot-nav"><span>Home</span><span>About Us</span><span>Services</span><span>FAQs</span><span>Contact Us</span></div>
  <div class="foot-cols">
    <div class="foot-col">
      <div class="ico"><svg width="24" height="24" viewBox="0 0 24 24"><path d="M6 3l3 .3 1.2 3.8-1.9 1.5a10 10 0 004.7 4.7l1.5-1.9 3.8 1.2.3 3a2 2 0 01-2.2 2A15.5 15.5 0 014 5.2 2 2 0 016 3z" fill="#fff"/></svg></div>
      <div><b>Phone:</b> 0333 410 7265</div>
      <div><b>Fax:</b> 0333 410 7265</div>
    </div>
    <div class="foot-col">
      <div class="ico"><svg width="24" height="24" viewBox="0 0 24 24"><rect x="3" y="6" width="18" height="13" rx="2" fill="#fff"/><path d="M3.5 7l8.5 6 8.5-6" stroke="#1b1e4b" stroke-width="1.6" fill="none"/></svg></div>
      <div><b>Email:</b></div>
      <div>info@kelmora-utilitylink.com</div>
    </div>
    <div class="foot-col">
      <div class="ico"><svg width="24" height="24" viewBox="0 0 24 24"><path d="M12 2a7 7 0 017 7c0 5-7 13-7 13S5 14 5 9a7 7 0 017-7z" fill="#fff"/><circle cx="12" cy="9" r="2.6" fill="#1b1e4b"/></svg></div>
      <div>Unit 4, 12 Harrow</div>
      <div>Lane, Leicester, LE2 7QS</div>
    </div>
  </div>
  <div class="copy">2022 Kelmora UtilityLink. All Rights Reserved.</div>
</footer>

</div>
</body>
</html>
```